Product Label Design

Spice Pots (www.spicepots.com.au) is a subsidiary unit of Maroon Orchard Indian Restaurant (www.maroonorchard.com.au) . We need a product label 35mm (h)x 100mm (w) . The label should include both logos of spice pots and maroon orchard, a barcode and product name (ex butter chicken) and Allergan info ( Gluten-free, dairy-free, nut-free). Logos uploaded.

Target Market(s)

Food and Retail

Colors

Designer to choose colors to be used in the design.

Requirements
Must have
• Refer Project description
Nice to have
Should not have

```html
<!DOCTYPE html>
<html lang="en">
<head>
<meta charset="utf-8">
<title>Spice Pots Butter Chicken Label</title>
<link rel="stylesheet" href="https://fonts.googleapis.com/css2?family=DM+Serif+Display&family=PT+Sans+Narrow&family=Montserrat:wght@600&family=Playfair+Display:wght@700&display=swap">
<style>
  :root {
    --label-red: #ec2029;
    --label-white: #ffffff;
    --sun-yellow: #f5b719;
    --spice-orange: rgba(236, 120, 24, 0.82);
    --curry-maroon: #5c120c;
    --brand-maroon: #b3232c;
    --ink: #1a1a1a;
    --curry-deep: #c4501c;
    --curry-light: #e88a3c;
  }
  * { margin: 0; padding: 0; box-sizing: border-box; }
  html, body { width: 1200px; height: 443px; overflow: hidden; background: var(--label-white); }
  .label { position: relative; width: 1200px; height: 443px; overflow: hidden; background: var(--label-red); }
  .label-shapes { position: absolute; inset: 0; }
  .intro-copy {
    position: absolute; left: 43px; top: 42px; width: 248px;
    font-family: "PT Sans Narrow", sans-serif; font-size: 15.5px; line-height: 20.7px;
    color: var(--label-white); text-align: justify;
  }
  .code-panel { position: absolute; left: 47px; top: 283px; width: 205px; height: 79px; background: var(--label-white); }
  .restaurant-name {
    position: absolute; left: 420px; top: 48px; width: 320px; text-align: center;
    font-family: "DM Serif Display", serif; font-size: 36px; line-height: 1; color: var(--brand-maroon);
  }
  .pots-brand {
    position: absolute; left: 548px; top: 160px; display: flex; align-items: center; gap: 6px;
    font-family: "DM Serif Display", serif; font-size: 20px; color: var(--brand-maroon);
  }
  .pots-brand .dot { width: 10px; height: 10px; border-radius: 50%; background: var(--brand-maroon); }
  .dish-photo {
    position: absolute; left: 628px; top: 118px; width: 300px; height: 250px; border-radius: 50%;
    background: radial-gradient(circle at 45% 50%, var(--curry-light) 0%, var(--curry-deep) 62%, #9a8a78 64%, #d8d2cc 72%, rgba(255,255,255,0) 74%);
  }
  .product-name {
    position: absolute; left: 423px; top: 222px;
    font-family: "DM Serif Display", serif; font-size: 76px; line-height: 62px; color: var(--curry-maroon);
  }
  .detail-copy {
    position: absolute; left: 940px; top: 38px; width: 213px;
    font-family: "PT Sans Narrow", sans-serif; font-size: 16px; line-height: 25.2px;
    color: var(--ink); text-align: justify;
  }
  .tagline {
    position: absolute; left: 940px; top: 318px; width: 230px;
    font-family: "Playfair Display", serif; font-weight: 700; font-size: 18px; line-height: 22px; color: var(--curry-maroon);
  }
  .allergen-band {
    position: absolute; left: 325px; top: 367px; width: 875px; height: 37px; background: var(--label-red);
    display: flex; align-items: center; padding-left: 60px; gap: 14px;
    font-family: "Montserrat", sans-serif; font-weight: 600; font-size: 21px; color: var(--label-white);
  }
</style>
</head>
<body>
<main class="label">
  <svg class="label-shapes" width="1200" height="443" viewBox="0 0 1200 443">
    <path d="M525 0 C420 70 328 210 325 443 L1200 443 L1200 0 Z" fill="var(--label-white)"/>
    <circle cx="500" cy="372" r="178" fill="var(--sun-yellow)"/>
    <circle cx="336" cy="258" r="64" fill="var(--spice-orange)"/>
    <circle cx="533" cy="151" r="9" fill="var(--label-red)"/>
  </svg>

  <p class="intro-copy">Is simply dummy text of the printing and typesetting industry. Lorem Ipsum has been the industry's standard dummy text ever since the 1500s, when an unknown printer took a galley of type and scrambled it to make a type specimen book. It has survived not only five centuries, but also the leap into electronic typesetting.</p>
  <div class="code-panel"></div>

  <div class="restaurant-name">Maroon Orchard</div>
  <div class="pots-brand"><span class="dot"></span>Spice Pots</div>

  <div class="dish-photo" role="img" aria-label="Photo of butter chicken curry in a copper serving bowl with cream and coriander"></div>

  <h1 class="product-name">Butter<br>Chicken</h1>

  <p class="detail-copy">Is simply dummy text of the printing and typesetting industry. Lorem Ipsum has been the industry's standard dummy text ever since the 1500s, when an unknown printer took a galley of type and scrambled it to make a type specimen book. It has survived not only five centuries, but also the leap into electronic typesetting.</p>
  <p class="tagline">Remaining Essentially Unchanged.</p>

  <div class="allergen-band">
    <span>Gluten-free</span><span>•</span><span>Dairy-free</span><span>•</span><span>Nut-free</span>
  </div>
</main>
</body>
</html>
```